Feather Meadow Wild Bird Food Gusset Bag Deisgn

We’re looking to transition from our current packaging—using a sticker on a bag—to a fully printed film design. The goal is to modernize the look and make it more fun while staying true to our existing brand identity.
We’d like to retain the same color scheme, fonts, and artwork style currently used on our bags. The barcode and product information should be placed on the back of the bag.
Bag specifications:
Dimensions: 410mm (length) x 530mm (width)
Design: Predominantly white with strategically placed transparent areas to allow the product to be seen inside.
There are 10 different bag designs required for this range.
We have attached our current labels of each product there is a Circle one and also a rectangle one that all all product information
We would also likes explained and also a image showing the these 5L bags refill 5L Tubs
We’ll also attach some example bags that represent the look and feel we’re aiming for in the new designs.
The bag is a gusset bag, Icon attached as an example
Target Market(s)
Wild Bird Food Buyers
Look and feel

```html
<!DOCTYPE html>
<html lang="en">
<head>
<meta charset="utf-8">
<title>Feather Meadow – Wild Bird Food Bag Range</title>
<link href="https://fonts.googleapis.com/css2?family=Chewy&family=Oswald:wght@500&display=swap" rel="stylesheet">
<style>
  :root{
    --bg-top:#fbfcf9;
    --bg-mid:#dcebc6;
    --bg-bottom:#8fbf48;
    --bag-white:#ffffff;
    --gusset-light:#f4f4f4;
    --gusset-dark:#dedede;
    --peanut:#b07a3a;
    --mealworm:#8a361d;
    --sunflower:#141414;
    --brand-teal:#1f8a80;
    --brand-green:#7cb63a;
    --warn-red:#d52b2b;
    --ink:#2a2a2a;
    --callout:#f2f20a;
    --label-white:#ffffff;
    --window-peanut:#8a8d93;
    --window-mealworm:#b86a35;
    --window-sunflower:#6d6a62;
  }
  *{box-sizing:border-box;margin:0;padding:0}
  html,body{width:1200px;height:1000px;overflow:hidden}
  body{
    background:linear-gradient(180deg,var(--bg-top) 0%,var(--bg-mid) 45%,var(--bg-bottom) 100%);
    font-family:"Oswald",sans-serif;
    position:relative;
  }

  /* bag */
  .bag{position:absolute;top:230px;width:340px;height:570px;display:flex;
    filter:drop-shadow(0 10px 18px rgba(0,0,0,.18))}
  .bag--peanuts{left:57px;--accent:var(--peanut);--window:var(--window-peanut)}
  .bag--mealworms{left:428px;--accent:var(--mealworm);--window:var(--window-mealworm)}
  .bag--sunflower{left:800px;--accent:var(--sunflower);--window:var(--window-sunflower)}

  .bag__front{position:relative;width:262px;height:100%;background:var(--bag-white);
    border-radius:12px 0 0 6px;overflow:hidden}
  .bag__gusset{position:relative;width:78px;height:100%;
    background:linear-gradient(90deg,var(--gusset-light),var(--gusset-dark));
    border-radius:0 12px 6px 0;overflow:hidden}
  .bag__band{height:130px;background:var(--accent)}
  .bag__gusset .bag__band{height:70px}

  .bag__brand{position:absolute;top:98px;left:50%;transform:translateX(-50%);
    width:140px;height:62px;background:var(--bag-white);
    border:3px solid var(--brand-green);border-radius:3px;
    display:flex;align-items:center;justify-content:center;gap:6px}
  .bag__brand-dot{width:12px;height:12px;border-radius:50%;background:var(--brand-teal);flex:none}
  .bag__brand-name{font-family:"Oswald",sans-serif;font-weight:500;font-size:15px;line-height:1;color:var(--brand-teal)}

  .bag__title{position:absolute;top:178px;left:0;right:0;text-align:center;
    font-family:"Chewy",system-ui,sans-serif;font-weight:400;color:var(--accent);line-height:.95}
  .bag__title--one{top:186px;font-size:54px}
  .bag__title--two{top:160px;font-size:40px}

  .bag__window{position:absolute;top:268px;left:22px;width:220px;height:180px;
    border-radius:90px 90px 40px 40px;background:var(--window)}

  .bag__icons{position:absolute;left:10px;bottom:34px;display:flex;gap:6px}
  .icon{width:36px;text-align:center;font-size:6.5px;line-height:1.1;color:var(--ink)}
  .icon svg{display:block;margin:0 auto 2px}
  .bag__info{position:absolute;right:20px;bottom:38px;text-align:right;font-size:10px;line-height:1.45;color:var(--ink)}

  /* gusset content */
  .gusset__icons{position:absolute;top:100px;left:0;right:0;display:flex;flex-direction:column;align-items:center;gap:12px}
  .gusset__icons .icon{width:50px;font-size:5px}
  .gusset__composition{position:absolute;top:290px;left:0;right:0;text-align:center;font-size:6px;line-height:1.3;color:var(--ink)}
  .gusset__composition b{display:block;color:var(--brand-teal);font-weight:500}
  .gusset__info{position:absolute;top:362px;left:0;right:0;text-align:center;font-size:6px;line-height:1.4;color:var(--ink)}
  .gusset__fields{position:absolute;top:392px;left:12px;right:10px;display:flex;flex-direction:column;gap:4px}
  .field{display:flex;align-items:center;justify-content:flex-end;gap:3px;font-size:5px;color:var(--ink)}
  .field__box{width:30px;height:11px;border:1px solid var(--ink)}

  /* presentation callouts */
  .callouts{position:absolute;inset:0;pointer-events:none;z-index:2}
  .callout-tub{position:absolute;left:744px;top:86px;width:80px;text-align:center;z-index:3}
  .callout-tub__text{font-size:13px;line-height:1.15;color:var(--ink);margin-top:4px}
  .callout-window{position:absolute;left:418px;top:808px;font-size:22px;color:var(--label-white);z-index:3}
</style>
</head>
<body>

<section class="bag bag--peanuts">
  <div class="bag__front">
    <div class="bag__band"></div>
    <div class="bag__brand"><span class="bag__brand-dot"></span><span class="bag__brand-name">Feather Meadow</span></div>
    <h2 class="bag__title bag__title--one">Peanuts</h2>
    <div class="bag__window" role="img" aria-label="Transparent bird-shaped window showing peanuts inside"></div>
    <div class="bag__icons">
      <div class="icon"><svg width="20" height="20" viewBox="0 0 26 26"><circle cx="13" cy="13" r="11" fill="#fff" stroke="#7cb63a" stroke-width="2.5"/><path d="M7 10h12l-1.5 8h-9z" fill="#1f8a80"/></svg>5L bags refill 5L Tubs</div>
      <div class="icon"><svg width="20" height="20" viewBox="0 0 26 26"><circle cx="13" cy="13" r="11" fill="#fff" stroke="#d52b2b" stroke-width="2.5"/><line x1="6" y1="20" x2="20" y2="6" stroke="#d52b2b" stroke-width="2.5"/></svg>Not for human consumption</div>
      <div class="icon"><svg width="20" height="20" viewBox="0 0 26 26"><circle cx="13" cy="13" r="11" fill="#fff" stroke="#7cb63a" stroke-width="2.5"/><ellipse cx="13" cy="13" rx="4" ry="7" fill="#1f8a80" transform="rotate(-35 13 13)"/></svg>May Contain Nuts</div>
    </div>
    <div class="bag__info">Net Weight: 3100g<br>SKU: FM22</div>
  </div>
  <div class="bag__gusset">
    <div class="bag__band"></div>
    <div class="gusset__icons">
      <div class="icon"><svg width="22" height="22" viewBox="0 0 26 26"><circle cx="13" cy="13" r="11" fill="#fff" stroke="#7cb63a" stroke-width="2.5"/><path d="M7 10h12l-1.5 8h-9z" fill="#1f8a80"/></svg>5L bags refill 5L Tubs</div>
      <div class="icon"><svg width="22" height="22" viewBox="0 0 26 26"><circle cx="13" cy="13" r="11" fill="#fff" stroke="#d52b2b" stroke-width="2.5"/><line x1="6" y1="20" x2="20" y2="6" stroke="#d52b2b" stroke-width="2.5"/></svg>Not for human consumption</div>
      <div class="icon"><svg width="22" height="22" viewBox="0 0 26 26"><circle cx="13" cy="13" r="11" fill="#fff" stroke="#7cb63a" stroke-width="2.5"/><ellipse cx="13" cy="13" rx="4" ry="7" fill="#1f8a80" transform="rotate(-35 13 13)"/></svg>May Contain Nuts</div>
    </div>
    <p class="gusset__composition"><b>Composition:</b>Peanuts</p>
    <p class="gusset__info">Net Weight: 3100g<br>SKU: FM22</p>
    <div class="gusset__fields">
      <div class="field">Expiry Date:<span class="field__box"></span></div>
      <div class="field">Batch:<span class="field__box"></span></div>
    </div>
  </div>
</section>

<section class="bag bag--mealworms">
  <div class="bag__front">
    <div class="bag__band"></div>
    <div class="bag__brand"><span class="bag__brand-dot"></span><span class="bag__brand-name">Feather Meadow</span></div>
    <h2 class="bag__title bag__title--two">Dried<br>Mealworms</h2>
    <div class="bag__window" role="img" aria-label="Transparent bird-shaped window showing dried mealworms and seed inside"></div>
    <div class="bag__icons">
      <div class="icon"><svg width="20" height="20" viewBox="0 0 26 26"><circle cx="13" cy="13" r="11" fill="#fff" stroke="#7cb63a" stroke-width="2.5"/><path d="M7 10h12l-1.5 8h-9z" fill="#1f8a80"/></svg>5L bags refill 5L Tubs</div>
      <div class="icon"><svg width="20" height="20" viewBox="0 0 26 26"><circle cx="13" cy="13" r="11" fill="#fff" stroke="#d52b2b" stroke-width="2.5"/><line x1="6" y1="20" x2="20" y2="6" stroke="#d52b2b" stroke-width="2.5"/></svg>Not for human consumption</div>
      <div class="icon"><svg width="20" height="20" viewBox="0 0 26 26"><circle cx="13" cy="13" r="11" fill="#fff" stroke="#7cb63a" stroke-width="2.5"/><ellipse cx="13" cy="13" rx="4" ry="7" fill="#1f8a80" transform="rotate(-35 13 13)"/></svg>May Contain Nuts</div>
    </div>
    <div class="bag__info">Net Weight: 800g<br>SKU: FM23</div>
  </div>
  <div class="bag__gusset">
    <div class="bag__band"></div>
    <div class="gusset__icons">
      <div class="icon"><svg width="22" height="22" viewBox="0 0 26 26"><circle cx="13" cy="13" r="11" fill="#fff" stroke="#7cb63a" stroke-width="2.5"/><path d="M7 10h12l-1.5 8h-9z" fill="#1f8a80"/></svg>5L bags refill 5L Tubs</div>
      <div class="icon"><svg width="22" height="22" viewBox="0 0 26 26"><circle cx="13" cy="13" r="11" fill="#fff" stroke="#d52b2b" stroke-width="2.5"/><line x1="6" y1="20" x2="20" y2="6" stroke="#d52b2b" stroke-width="2.5"/></svg>Not for human consumption</div>
      <div class="icon"><svg width="22" height="22" viewBox="0 0 26 26"><circle cx="13" cy="13" r="11" fill="#fff" stroke="#7cb63a" stroke-width="2.5"/><ellipse cx="13" cy="13" rx="4" ry="7" fill="#1f8a80" transform="rotate(-35 13 13)"/></svg>May Contain Nuts</div>
    </div>
    <p class="gusset__composition"><b>Composition:</b>Dried Mealworms</p>
    <p class="gusset__info">Net Weight: 800g<br>SKU: FM23</p>
    <div class="gusset__fields">
      <div class="field">Expiry Date:<span class="field__box"></span></div>
      <div class="field">Batch:<span class="field__box"></span></div>
    </div>
  </div>
</section>

<section class="bag bag--sunflower">
  <div class="bag__front">
    <div class="bag__band"></div>
    <div class="bag__brand"><span class="bag__brand-dot"></span><span class="bag__brand-name">Feather Meadow</span></div>
    <h2 class="bag__title bag__title--two">Black<br>Sunflower</h2>
    <div class="bag__window" role="img" aria-label="Transparent bird-shaped window showing black sunflower seed inside"></div>
    <div class="bag__icons">
      <div class="icon"><svg width="20" height="20" viewBox="0 0 26 26"><circle cx="13" cy="13" r="11" fill="#fff" stroke="#7cb63a" stroke-width="2.5"/><path d="M7 10h12l-1.5 8h-9z" fill="#1f8a80"/></svg>5L bags refill 5L Tubs</div>
      <div class="icon"><svg width="20" height="20" viewBox="0 0 26 26"><circle cx="13" cy="13" r="11" fill="#fff" stroke="#d52b2b" stroke-width="2.5"/><line x1="6" y1="20" x2="20" y2="6" stroke="#d52b2b" stroke-width="2.5"/></svg>Not for human consumption</div>
      <div class="icon"><svg width="20" height="20" viewBox="0 0 26 26"><circle cx="13" cy="13" r="11" fill="#fff" stroke="#7cb63a" stroke-width="2.5"/><ellipse cx="13" cy="13" rx="4" ry="7" fill="#1f8a80" transform="rotate(-35 13 13)"/></svg>May Contain Nuts</div>
    </div>
    <div class="bag__info">Net Weight: 2000g<br>SKU: FM30</div>
  </div>
  <div class="bag__gusset">
    <div class="bag__band"></div>
    <div class="gusset__icons">
      <div class="icon"><svg width="22" height="22" viewBox="0 0 26 26"><circle cx="13" cy="13" r="11" fill="#fff" stroke="#7cb63a" stroke-width="2.5"/><path d="M7 10h12l-1.5 8h-9z" fill="#1f8a80"/></svg>5L bags refill 5L Tubs</div>
      <div class="icon"><svg width="22" height="22" viewBox="0 0 26 26"><circle cx="13" cy="13" r="11" fill="#fff" stroke="#d52b2b" stroke-width="2.5"/><line x1="6" y1="20" x2="20" y2="6" stroke="#d52b2b" stroke-width="2.5"/></svg>Not for human consumption</div>
      <div class="icon"><svg width="22" height="22" viewBox="0 0 26 26"><circle cx="13" cy="13" r="11" fill="#fff" stroke="#7cb63a" stroke-width="2.5"/><ellipse cx="13" cy="13" rx="4" ry="7" fill="#1f8a80" transform="rotate(-35 13 13)"/></svg>May Contain Nuts</div>
    </div>
    <p class="gusset__composition"><b>Composition:</b>Black Sunflower</p>
    <p class="gusset__info">Net Weight: 2000g<br>SKU: FM30</p>
    <div class="gusset__fields">
      <div class="field">Expiry Date:<span class="field__box"></span></div>
      <div class="field">Batch:<span class="field__box"></span></div>
    </div>
  </div>
</section>

<div class="callout-tub">
  <svg width="72" height="72" viewBox="0 0 72 72"><circle cx="36" cy="36" r="32" fill="#fff" stroke="#7cb63a" stroke-width="7"/><ellipse cx="36" cy="25" rx="20" ry="5" fill="#1f8a80"/><path d="M16 26h40l-4 22q-16 6-32 0z" fill="#1f8a80"/></svg>
  <p class="callout-tub__text">5L bags refill<br>5L Tubs</p>
</div>

<p class="callout-window">packaging window</p>

<svg class="callouts" width="1200" height="1000" viewBox="0 0 1200 1000" aria-hidden="true">
  <path d="M797 210 C 800 280, 780 320, 742 340" fill="none" stroke="var(--callout)" stroke-width="3"/>
  <path d="M742 340 l12 -2 M742 340 l4 -11" fill="none" stroke="var(--callout)" stroke-width="3"/>
  <path d="M410 822 C 340 800, 300 720, 262 630" fill="none" stroke="var(--callout)" stroke-width="3"/>
  <path d="M262 630 l-2 13 M262 630 l11 6" fill="none" stroke="var(--callout)" stroke-width="3"/>
</svg>

</body>
</html>
```